Business Card Design

I need a business card designed for my business.

The company name is Rowan Pellet Group

It has four brands underneath it. They are:
- RP Events
- RP Sports Tours
- RPG Management
- Bold Mosaic

I have attached all logo items, as well as our last business card.

I look forward to seeing your designs.

Industry/Entity Type

Business

Colors
eb1f27
0355a3

Requirements
Must have
• Our contact details as per the front page of our previous business card.

```html
<!DOCTYPE html>
<html lang="en">
<head>
<meta charset="utf-8">
<title>Rowan Pellet Group – Business Card</title>
<link rel="stylesheet" href="https://fonts.googleapis.com/css2?family=Mulish:wght@400;600;700;800&display=swap">
<style>
  :root {
    --brand-red: #eb1f27;
    --brand-blue: #0355a3;
    --navy: #0b4f8a;
    --mid-blue: #2a65a6;
    --soft-blue: #a7b9d6;
    --ink: #1d4f86;
    --white: #ffffff;
  }
  * { margin: 0; padding: 0; box-sizing: border-box; }
  html, body { width: 981px; height: 1200px; overflow: hidden; background: var(--white); }
  body { position: relative; font-family: "Mulish", sans-serif; color: var(--ink); }

  .card {
    position: absolute; left: 81px; width: 814px; height: 504px;
    border-radius: 28px; overflow: hidden;
    background: linear-gradient(100deg, #f4f7fb 0%, #ffffff 45%, #d9e5f1 100%);
    box-shadow: 6px 10px 18px rgba(0, 0, 0, 0.18);
  }
  .card--front { top: 63px; }
  .card--back { top: 613px; background: linear-gradient(260deg, #ffffff 30%, #f2f6fa 60%, #c9d9ea 100%); }

  .card__swoosh { position: absolute; inset: 0; width: 814px; height: 504px; }

  .card__footer {
    position: absolute; left: 0; right: 0; bottom: 0; height: 80px;
    background: var(--navy);
    display: flex; align-items: center; justify-content: center;
    color: var(--white); font-weight: 700; font-size: 24px; letter-spacing: 0.2px;
  }
  .card__footer::before {
    content: ""; position: absolute; left: 0; right: 0; top: -16px; height: 12px;
    background: linear-gradient(90deg, #9fc3e0, #e8f1f8 50%, #9fc3e0);
  }

  .decor-disc {
    position: absolute; border-radius: 50%;
    background: rgba(165, 190, 220, 0.25);
  }

  .group-mark { position: absolute; left: 230px; top: 38px; display: flex; align-items: center; gap: 22px; }
  .group-mark__dot { width: 92px; height: 92px; border-radius: 50%; background: var(--brand-blue); flex: none; }
  .group-mark__name { font-size: 40px; font-weight: 800; color: var(--brand-blue); line-height: 1; width: 380px; }

  .person { position: absolute; left: 383px; top: 188px; }
  .person__name { font-size: 28px; font-weight: 800; color: var(--navy); }
  .person__role { font-size: 24px; font-weight: 400; color: var(--ink); margin-top: 4px; }

  .address { position: absolute; left: 105px; top: 292px; font-size: 22px; line-height: 32px; color: var(--ink); font-style: normal; }
  .divider { position: absolute; left: 361px; top: 300px; width: 3px; height: 84px; background: var(--brand-red); }
  .contact { position: absolute; left: 385px; top: 290px; color: var(--ink); }
  .contact__phone { font-size: 25px; line-height: 34px; }
  .contact__email { font-size: 19px; line-height: 32px; }

  .brand {
    position: absolute; font-size: 31px; font-weight: 800; line-height: 1.1;
    display: flex; align-items: center; height: 76px; white-space: nowrap;
  }
  .brand--events { left: 48px; top: 74px; width: 280px; color: var(--navy); }
  .brand--tours { left: 364px; top: 74px; width: 270px; color: var(--brand-red); }
  .brand--management { left: 70px; top: 205px; width: 280px; color: var(--navy); }
  .brand--mosaic { left: 380px; top: 205px; width: 230px; color: var(--brand-red); }

  .follow { position: absolute; left: 160px; top: 352px; display: flex; align-items: center; gap: 12px; }
  .follow__label { font-size: 24px; color: var(--ink); margin-right: 10px; }
  .follow__icon { width: 46px; height: 46px; border-radius: 6px; background: var(--mid-blue); }
</style>
</head>
<body>

<section class="card card--front" aria-label="Business card front">
  <svg class="card__swoosh" viewBox="0 0 814 504" aria-hidden="true">
    <path d="M0 0 H262 C150 80 60 230 40 425 H0 Z" fill="#a7b9d6"/>
    <path d="M262 0 C150 80 60 230 40 425" fill="none" stroke="#ffffff" stroke-width="2"/>
    <path d="M262 0 H302 C172 90 92 240 72 425 H40 C60 230 150 80 262 0 Z" fill="#2a65a6"/>
    <path d="M302 0 H320 C192 95 108 245 88 425 H72 C92 240 172 90 302 0 Z" fill="#e53a2e"/>
  </svg>
  <div class="decor-disc" style="left:610px; top:10px; width:160px; height:160px;"></div>
  <div class="decor-disc" style="left:600px; top:190px; width:230px; height:230px;"></div>

  <div class="group-mark">
    <span class="group-mark__dot"></span>
    <span class="group-mark__name">Rowan Pellet Group</span>
  </div>

  <div class="person">
    <p class="person__name">Rowan Pellet</p>
    <p class="person__role">Principal</p>
  </div>

  <address class="address">
    PO Box 418<br>
    Kestrel Vale ACT 2690<br>
    Australia
  </address>
  <span class="divider"></span>
  <div class="contact">
    <p class="contact__phone">+ 61 2 5550 1840</p>
    <p class="contact__phone">+ 61 400 555 218</p>
    <p class="contact__email">Rowan@RowanPelletGroup.com.au</p>
  </div>

  <footer class="card__footer">www.RowanPelletGroup.com.au</footer>
</section>

<section class="card card--back" aria-label="Business card back">
  <svg class="card__swoosh" viewBox="0 0 814 504" aria-hidden="true">
    <g transform="translate(814 0) scale(-1 1)">
      <path d="M0 0 H262 C150 80 60 230 40 425 H0 Z" fill="#a7b9d6"/>
      <path d="M262 0 C150 80 60 230 40 425" fill="none" stroke="#ffffff" stroke-width="2"/>
      <path d="M262 0 H302 C172 90 92 240 72 425 H40 C60 230 150 80 262 0 Z" fill="#2a65a6"/>
      <path d="M302 0 H320 C192 95 108 245 88 425 H72 C92 240 172 90 302 0 Z" fill="#e53a2e"/>
    </g>
  </svg>
  <div class="decor-disc" style="left:40px; top:20px; width:130px; height:130px;"></div>
  <div class="decor-disc" style="left:250px; top:60px; width:200px; height:200px;"></div>

  <p class="brand brand--events">RP Events</p>
  <p class="brand brand--tours">RP Sports Tours</p>
  <p class="brand brand--management">RPG Management</p>
  <p class="brand brand--mosaic">Bold Mosaic</p>

  <div class="follow">
    <span class="follow__label">Follow Us On:</span>
    <span class="follow__icon" aria-hidden="true"></span>
    <span class="follow__icon" aria-hidden="true"></span>
    <span class="follow__icon" aria-hidden="true"></span>
  </div>

  <footer class="card__footer">www.RowanPelletGroup.com.au</footer>
</section>

</body>
</html>
```